IT-support company web-site design

We need to re-design out site for existing clients and for the future promotions. Site needs to be attractive with intuitive interface. We need to keep our logo and colors but any reshuffles can be made. I provide the working site and re-made version, which we do nt like. It has to be more bright and clear. All the blocks have to be divided and look like logic and structured. PLease find the addresses to work with below.
The "real" one https://plorim.com
The version http://dostuly.net/Plorim/
If you have any с

Industry/Entity Type

It Company

Number of Pages Required

5+ page

Font styles to use
Sans Serif

Colors
9bcb3c

Requirements
Must have
• Our LOGO and our colors (green palette). We d like to make our services blocks as the main things. We need to have our images and slogans as there are extremely important advantages of our company.
Nice to have
• Original and modern view of the site.
Should not have
• unpredictable and @surprising@, hard- definable buttons and ways

```html
<!DOCTYPE html>
<html lang="en">
<head>
<meta charset="utf-8">
<title>Plorim – IT Support</title>
<link href="https://fonts.googleapis.com/css2?family=Mulish:wght@400;600;700;800&display=swap" rel="stylesheet">
<style>
:root{
  --green:#9bcb3c;
  --green-2:#6fcf97;
  --ink:#333;
  --muted:#666;
  --light:#f0f0f0;
  --card:#ededed;
  --line:#d6d6d6;
  --white:#fff;
  --arrow:#3d4148;
}
*{box-sizing:border-box;margin:0;padding:0}
html,body{width:1200px;height:2394px;overflow:hidden}
body{position:relative;background:var(--white);font-family:'Mulish',sans-serif;color:var(--ink)}
.abs{position:absolute}
.brand{display:flex;align-items:center;gap:12px;font-size:34px;font-weight:400;color:#4a4a4a;letter-spacing:1px}
.brand-dot{width:26px;height:26px;border-radius:50%;border:2px solid var(--green-2)}
.header .brand{left:99px;top:22px}
.tagline{left:456px;top:32px;font-size:22px;color:#8a8a8a;letter-spacing:.5px}
.login{left:843px;top:0;width:258px;height:83px;background:var(--green);color:var(--white);display:flex;align-items:center;justify-content:center;gap:12px;font-size:21px;font-weight:700}
.nav{left:0;top:83px;width:1200px;height:57px;background:var(--light)}
.nav ul{list-style:none;display:flex;position:absolute;left:99px;top:0;height:57px}
.nav li{font-size:14px;font-weight:600;color:#222;display:flex;align-items:center;padding:0 15px}
.nav li.active{background:var(--green);color:var(--white);padding:0 22px}
.nav .search{right:99px;top:17px}
.hero{left:0;top:140px;width:1200px;height:490px;background:linear-gradient(120deg,#5b6a78 0%,#2c3138 40%,#5a4436 65%,#1c1e22 100%);clip-path:polygon(0 0,100% 0,100% 88%,0 100%)}
.hero-inner{left:0;top:140px;width:1200px;text-align:center;color:var(--white)}
.deco-ring{width:30px;height:30px;border-radius:50%;border:2px solid currentColor;margin:0 auto}
.hero-inner .deco-ring{margin-top:92px;color:var(--green-2)}
.hero-title{font-size:35px;font-weight:700;margin-top:32px;letter-spacing:.5px}
.hero-sub{font-size:16px;line-height:32px;margin-top:8px}
.btn-green{display:inline-block;background:linear-gradient(90deg,var(--green),var(--green-2));color:var(--white);font-weight:700;border-radius:20px}
.hero-inner .btn-green{margin-top:20px;padding:10px 24px;font-size:15px}
.slide-arrow{width:48px;height:50px;background:var(--arrow);display:flex;align-items:center;justify-content:center}
.clients{left:99px;top:662px;width:1002px;height:72px;display:flex;align-items:center;justify-content:space-between}
.client{font-size:22px;font-weight:800;color:#1c4f7a}
.client.small{font-size:15px;font-weight:600;color:#333}
.divider{left:99px;top:771px;width:1002px;height:1px;background:var(--line)}
.section-title{width:1200px;left:0;text-align:center;font-size:23px;letter-spacing:4px;font-weight:600;color:#444}
.underline{left:570px;width:60px;height:3px;background:var(--green)}
.card{top:875px;width:236px;height:271px;background:var(--card);text-align:center}
.card.selected{background:var(--white);border:1px solid var(--green)}
.card svg{margin-top:25px}
.card p{font-size:15px;line-height:21px;color:#333;margin-top:22px;padding:0 20px}
.card .plus{position:absolute;right:0;bottom:0;width:30px;height:30px;background:var(--green);color:var(--white);font-size:22px;line-height:28px}
.dots{left:586px;top:1171px;display:flex;gap:9px}
.dots span{width:7px;height:7px;border-radius:50%;background:var(--green)}
.band{left:0;top:1200px;width:1200px;height:420px;background:linear-gradient(100deg,#9bcb3c 0%,#88cf6c 50%,#6fcf97 100%)}
.band-inner{left:0;top:1200px;width:1200px;text-align:center;color:var(--white)}
.band-inner .deco-ring{margin-top:74px}
.quote{font-size:23px;font-weight:700;letter-spacing:4px;line-height:26px;width:760px;margin:40px auto 0}
.btn-white{display:inline-block;margin-top:38px;background:linear-gradient(#fff,#e4e4e4);color:#333;font-weight:700;font-size:17px;padding:10px 22px;border-radius:22px}
.testimonial{left:150px;top:1796px;width:900px;text-align:center}
.t-company{font-size:14px;font-weight:700;letter-spacing:2.5px;color:#444}
.t-body{font-size:11.5px;line-height:21px;color:#444;margin-top:16px}
.t-author{font-size:13px;color:#555;margin-top:18px}
.t-arrows{left:560px;top:1979px;display:flex;gap:4px}
.t-arrows span{width:38px;height:42px;background:#9aa0a6;display:flex;align-items:center;justify-content:center}
.newsletter{left:0;top:2075px;width:1200px;height:204px;background:var(--light)}
.field{left:332px;top:2180px;width:351px;height:35px;background:var(--white);font-size:12px;letter-spacing:2px;color:#aaa;padding:11px 24px}
.field svg{position:absolute;right:16px;top:12px}
.subscribe{left:693px;top:2180px;width:182px;height:36px;border-radius:18px;font-size:16px;font-weight:600;display:flex;align-items:center;justify-content:center}
.footer .brand{left:99px;top:2294px;font-size:30px}
.social{left:99px;top:2346px;display:flex;gap:10px}
.social span{width:24px;height:24px;display:block}
.flinks{right:99px;top:2303px;display:flex;gap:30px;font-size:13.5px;color:#333}
.flinks b{font-weight:700}
.copyright{right:99px;top:2339px;font-size:10.5px;color:#333}
</style>
</head>
<body>
<header class="header">
  <div class="abs brand"><span class="brand-dot"></span>PLORIM</div>
  <div class="abs tagline">WE MAKE IT SIMPLE AND SECURE</div>
  <div class="abs login">
    <svg width="16" height="20" viewBox="0 0 16 20"><circle cx="8" cy="5" r="5" fill="#fff"/><path d="M0 20 Q0 11 8 11 Q16 11 16 20Z" fill="#fff"/></svg>
    Customer Login
  </div>
</header>
<nav class="abs nav">
  <ul>
    <li class="active">PLORIM DIFFERENCE</li><li>SERVICES</li><li>RESOURCES</li><li>CUSTOMERS</li><li>SUPPORT</li><li>CONTACT US</li>
  </ul>
  <svg class="abs search" width="22" height="22" viewBox="0 0 22 22"><circle cx="9" cy="9" r="7" fill="none" stroke="#555" stroke-width="3"/><line x1="14" y1="14" x2="20" y2="20" stroke="#555" stroke-width="3"/></svg>
</nav>

<div class="abs hero" role="img" aria-label="Photo of colleagues working together on a tablet"></div>
<div class="abs hero-inner">
  <div class="deco-ring"></div>
  <h1 class="hero-title">FREEDOM FROM IT WORRIES</h1>
  <p class="hero-sub">Your company does not need to buy any expensive equipment,<br>and your data will always be safe and secure at our Tier-4 data centers</p>
  <span class="btn-green">LEARN MORE</span>
</div>
<div class="abs slide-arrow" style="left:102px;top:302px"><svg width="12" height="18"><path d="M10 2 L3 9 L10 16" fill="none" stroke="#fff" stroke-width="2"/></svg></div>
<div class="abs slide-arrow" style="left:1053px;top:302px"><svg width="12" height="18"><path d="M2 2 L9 9 L2 16" fill="none" stroke="#fff" stroke-width="2"/></svg></div>

<svg class="abs" style="left:98px;top:690px" width="12" height="18"><path d="M10 2 L3 9 L10 16" fill="none" stroke="#222" stroke-width="2"/></svg>
<div class="abs clients" style="left:180px;width:840px">
  <span class="client">HALDEN BROOKS</span>
  <span class="client small">Ferris Quill<br>Ambrose &amp; Tate</span>
  <span class="client small">BAYWELL</span>
  <span class="client small">Norvale Home</span>
  <span class="client">DRANMORE</span>
</div>
<svg class="abs" style="left:1090px;top:690px" width="12" height="18"><path d="M2 2 L9 9 L2 16" fill="none" stroke="#222" stroke-width="2"/></svg>
<div class="abs divider"></div>

<h2 class="abs section-title" style="top:806px">OUR SERVICES</h2>
<div class="abs underline" style="top:849px"></div>

<div class="abs card" style="left:99px">
  <svg width="120" height="120" viewBox="0 0 120 120"><circle cx="60" cy="60" r="55" fill="none" stroke="#8fcf6a" stroke-width="6"/><rect x="44" y="40" width="32" height="40" rx="3" fill="none" stroke="#8fcf6a" stroke-width="3"/><line x1="51" y1="52" x2="69" y2="52" stroke="#8fcf6a" stroke-width="3"/><line x1="51" y1="60" x2="69" y2="60" stroke="#8fcf6a" stroke-width="3"/><line x1="51" y1="68" x2="69" y2="68" stroke="#8fcf6a" stroke-width="3"/></svg>
  <p>Freedom From IT Worries</p>
</div>
<div class="abs card selected" style="left:353px">
  <svg width="120" height="120" viewBox="0 0 120 120"><defs><linearGradient id="g1" x1="0" x2="1"><stop offset="0" stop-color="#9bcb3c"/><stop offset="1" stop-color="#6fcf97"/></linearGradient></defs><circle cx="60" cy="60" r="58" fill="url(#g1)"/><path d="M60 34 L80 42 V60 Q80 76 60 86 Q40 76 40 60 V42Z" fill="none" stroke="#fff" stroke-width="3"/><path d="M51 60 L58 67 L70 53" fill="none" stroke="#fff" stroke-width="3"/></svg>
  <p>Work Securely from Anywhere, Anytime.</p>
  <span class="plus">+</span>
</div>
<div class="abs card" style="left:610px">
  <svg width="120" height="120" viewBox="0 0 120 120"><circle cx="60" cy="60" r="55" fill="none" stroke="#8fcf6a" stroke-width="6"/><path d="M46 40 L54 40 L58 50 L53 54 Q57 64 66 67 L70 62 L80 66 L80 74 Q78 80 70 80 Q48 76 40 52 Q40 42 46 40Z" fill="none" stroke="#8fcf6a" stroke-width="3"/></svg>
  <p>Houston-based 24/7<br>Help Desk Support</p>
</div>
<div class="abs card" style="left:865px">
  <svg width="120" height="120" viewBox="0 0 120 120"><circle cx="60" cy="60" r="55" fill="none" stroke="#8fcf6a" stroke-width="6"/><circle cx="60" cy="62" r="22" fill="none" stroke="#8fcf6a" stroke-width="3"/><text x="60" y="72" text-anchor="middle" font-family="Mulish,sans-serif" font-size="28" font-weight="700" fill="#8fcf6a">$</text></svg>
  <p>Eliminate Unpredictable<br>IT Expenses.Reduce IT Costs</p>
</div>
<div class="abs dots"><span></span><span></span></div>

<div class="abs band" role="img" aria-label="Photo of hands working on a laptop, tinted green"></div>
<div class="abs band-inner">
  <div class="deco-ring"></div>
  <p class="quote">IT TECHNOLOGY WILL EVENTUALLY DELIVER ITS GREATEST VALUE TO AMERICAN BUSINESS WHEN IT BECOMES INVISIBLE TO USERS, WHEN IT CAN BE TAKEN FOR GRANTED.</p>
  <span class="btn-white">Get In Touch With Us</span>
</div>

<h2 class="abs section-title" style="top:1674px">TESTIMONIALS</h2>
<div class="abs underline" style="top:1717px"></div>
<div class="abs deco-ring" style="left:585px;top:1744px;color:var(--green-2)"></div>
<div class="abs testimonial">
  <p class="t-company">FERRIS, QUILL, AMBROSE &amp; TATE, LLC</p>
  <p class="t-body">Through the variety of services offered and their knowledgeable, professional, and friendly staff, PLORIM provides our company with a true partner for our IT needs. PLORIM saves us time and money – top items on any business owner's list. FQAT has had a business relationship with PLORIM since our firm had to temporarily relocate to Houston after Hurricane Katrina in 2005. Everyone at PLORIM has always been quick to help and educate along the way so that we are not only getting a problem solved, we are helping each other out to continue to build an efficient partnership for both companies.</p>
  <p class="t-author">-Lena Marsh, FQAT</p>
</div>
<div class="abs t-arrows">
  <span><svg width="10" height="14"><path d="M8 2 L3 7 L8 12" fill="none" stroke="#fff" stroke-width="2"/></svg></span>
  <span><svg width="10" height="14"><path d="M2 2 L7 7 L2 12" fill="none" stroke="#fff" stroke-width="2"/></svg></span>
</div>

<section class="abs newsletter">
  <h2 class="abs section-title" style="top:48px;font-weight:400;font-size:21px">NEWSLETTER SUBSCRIBE</h2>
</section>
<div class="abs field">ENTER EMAIL ID
  <svg width="13" height="10" viewBox="0 0 13 10"><rect x="0.5" y="0.5" width="12" height="9" fill="none" stroke="#555"/><path d="M0.5 0.5 L6.5 5.5 L12.5 0.5" fill="none" stroke="#555"/></svg>
</div>
<div class="abs btn-green subscribe">SUBSCRIBE</div>

<footer class="footer">
  <div class="abs brand"><span class="brand-dot"></span>PLORIM</div>
  <div class="abs social" aria-label="Social links">
    <span style="background:#3b5998"></span><span style="background:#40a9e0"></span><span style="background:#d9493a"></span><span style="background:#6b4f3a"></span>
  </div>
  <div class="abs flinks"><b>PLORIM DIFFERENCE</b><span>SERVICES</span><span>RESOURCES</span><span>CUSTOMERS</span><span>SUPPORT</span><span>CONTACT US</span></div>
  <div class="abs copyright">© 2017 .www.plorim.com &nbsp;|&nbsp; All Rights Reserved.</div>
</footer>
</body>
</html>
```